Design some Business Cards

Need some business cards made for new venture - website is varimest.com. I want to incorporate (in some fashion):

- logo (provided with name, and alone)
- website <p> font (Arvo )

Brian T. Holloway
BH VARIMEST
819 N. Garrick Ave. 3rd Floor
Chicago, IL 60647
brianh@varimest.com
(312) 448-2096
varimest.com

I am not very creative, hence the contest. Feel free to add design elements, but keep things consistent with the website (naturally). I am indifferent to one side vs. two-sided business card. I will be using PressNova, so you will want to use their Illustrator (or photoshop) templates located here:

http://www.pressnova-example.com/pn/ns/prodir/FileResources.aspx?pf_id=C41&selectedTab=0

The work product will be an Illustrator or Photoshop file, using the templates, with the winning design.

```html
<!DOCTYPE html>
<html lang="en">
<head>
<meta charset="utf-8">
<title>Varimest Business Cards</title>
<link rel="stylesheet" href="https://fonts.googleapis.com/css2?family=Open+Sans:wght@400;600;700&display=swap">
<style>
  :root {
    --backdrop: #4a4a4a;
    --card-light-top: #f7f7f7;
    --card-light-bottom: #dedede;
    --card-dark: #121212;
    --ink: #333333;
    --ink-soft: #555555;
    --rule: #444444;
    --mark-light: #d2d2d2;
  }
  * { margin: 0; padding: 0; box-sizing: border-box; }
  html, body {
    width: 1200px;
    height: 1153px;
    overflow: hidden;
    background: var(--backdrop);
    font-family: "Open Sans", Arial, sans-serif;
  }
  .canvas { position: relative; width: 1200px; height: 1153px; }

  .card { position: absolute; width: 608px; height: 347px; }
  .card--front {
    left: 300px; top: 191px;
    background: linear-gradient(160deg, var(--card-light-top), var(--card-light-bottom));
    color: var(--ink);
  }
  .card--back {
    left: 300px; top: 600px;
    background: var(--card-dark);
  }

  .front-mark {
    position: absolute; left: 44px; top: 38px;
    display: flex; align-items: center; gap: 10px;
    color: var(--ink);
    font-weight: 600; font-size: 17px; letter-spacing: 1px;
  }
  .front-mark .dot {
    width: 44px; height: 44px; border-radius: 50%;
    background: var(--ink);
  }

  .holder { position: absolute; left: 29px; top: 218px; }
  .holder__name { font-size: 21px; font-weight: 700; line-height: 1.2; color: var(--ink); }
  .holder__title { font-size: 18px; font-weight: 400; line-height: 1.2; color: var(--ink-soft); letter-spacing: 0.3px; }
  .holder__rule { width: 72px; height: 4px; background: var(--rule); margin-top: 8px; }

  .contact {
    position: absolute; left: 29px; top: 280px;
    font-size: 13px; line-height: 18px; color: var(--ink);
  }
  .contact .sep { font-weight: 700; margin: 0 6px; }

  .back-mark {
    position: absolute; left: 203px; top: 240px;
    display: flex; align-items: center; height: 72px;
  }
  .back-mark .dot {
    width: 56px; height: 56px; border-radius: 50%;
    background: var(--mark-light);
  }
  .back-mark .divider {
    width: 2px; height: 70px; background: var(--mark-light);
    margin: 0 20px 0 30px;
  }
  .back-mark .name {
    font-size: 50px; font-weight: 600; color: var(--mark-light);
    line-height: 1; letter-spacing: 0.5px;
  }
</style>
</head>
<body>
<main class="canvas">
  <section class="card card--front">
    <div class="front-mark"><span class="dot"></span><span>VARIMEST</span></div>
    <div class="holder">
      <p class="holder__name">Brian T. Holloway</p>
      <p class="holder__title">BH VARIMEST</p>
      <div class="holder__rule"></div>
    </div>
    <div class="contact">
      <p>(312) 448-2096</p>
      <p>brianh@varimest.com<span class="sep">|</span>varimest.com<span class="sep">|</span>819 N. Garrick Ave. 3rd Floor Chicago, IL 60647</p>
    </div>
  </section>

  <section class="card card--back">
    <div class="back-mark">
      <span class="dot"></span>
      <span class="divider"></span>
      <span class="name">varimest</span>
    </div>
  </section>
</main>
</body>
</html>
```